Fernhill Skin Studio is a rebranding of fernhillfootcare.com.au. The business provides Medical Injectables (botox and fillers) Laser and IPL therapies, Podiatry and remedial massage. We have a logo already done (yay! pixel guild!) you can download it here: http://fernhillskinstudio.com/brand_assets.zip . We are after a clean, long scrolling website (in the style of qrvlt.com). There will be 6 subpages (or sections depending on how you create it) (1) Cosmetic Injections (2) Podiatry (3) Remedial Massage (4) Laser Therapies (5) Skin Care (6) Customer Club and Special Offers. The target demographic is wealthy or aspirational women 35+.

Font styles to use
Sans Serif

Colors
9bcb3c
33a6d7

Requirements
Must have
• Simple, clean long scroller like qrvlt.com
Nice to have
• Congruence with existing corporate identity.

```html
<!DOCTYPE html>
<html lang="en">
<head>
<meta charset="utf-8">
<title>Fernhill Skin Studio</title>
<link href="https://fonts.googleapis.com/css2?family=Open+Sans:wght@300;400;600&display=swap" rel="stylesheet">
<style>
:root{
  --green:#9bcb3c;
  --blue:#33a6d7;
  --ink:#3a3a3a;
  --muted:#8a8a8a;
  --paper:#ffffff;
  --soft:#f2f2f2;
  --panel:#e6e6e6;
  --dark:#3b3937;
  --footer:#f7f7f7;
}
*{margin:0;padding:0;box-sizing:border-box}
html,body{width:1200px;height:3429px;overflow:hidden}
body{font-family:"Open Sans",Arial,sans-serif;color:var(--ink);background:var(--paper);position:relative}
section,header,footer{position:absolute;left:0;width:1200px;overflow:hidden}
.abs{position:absolute}
.center{left:0;width:1200px;text-align:center}
.photo{position:absolute;inset:0}
.mark{width:34px;height:34px;border-radius:50%;background:var(--green)}

/* hero */
.hero{top:0;height:657px}
.hero .photo{background:radial-gradient(ellipse at 50% 45%,#6d6a63 0%,#45423d 55%,#2a2826 100%)}
.hero .shade{position:absolute;inset:0;background:rgba(20,20,20,.25)}
.nav-brand{left:150px;top:38px;font-size:13px;font-weight:400;color:var(--paper)}
.nav{right:171px;top:42px;display:flex;gap:24px;list-style:none}
.nav li{font-size:10.5px;color:var(--paper);text-transform:uppercase;white-space:nowrap}
.nav-rule{left:150px;top:86px;width:900px;height:1px;background:rgba(255,255,255,.35)}
.hero-brand{top:230px;font-size:62px;font-weight:300;color:var(--paper);letter-spacing:6px;text-transform:uppercase}
.hero-tag{top:415px;font-size:18px;font-weight:300;color:var(--paper);letter-spacing:.5px}
.hero-title{top:440px;font-size:58px;font-weight:300;color:var(--paper);letter-spacing:1px}
.btn{background:var(--green);color:var(--paper);font-size:15px;text-transform:uppercase;display:flex;align-items:center;justify-content:center}
.hero .btn{left:466px;top:557px;width:268px;height:57px}

/* headings */
.sec-title{font-size:36px;font-weight:300;color:var(--ink);text-transform:uppercase}
.sec-sub{font-size:13px;color:var(--muted);text-transform:uppercase;letter-spacing:1px}

/* welcome */
.welcome{top:657px;height:494px;background:var(--paper)}
.service{position:absolute;top:250px;width:200px;text-align:center}
.service svg{width:100px;height:100px}
.service h3{font-size:16px;font-weight:400;text-transform:uppercase;margin-top:26px}
.service p{font-size:11px;line-height:16px;color:var(--muted);margin-top:10px}

/* feature bands */
.band-dark .photo{background:linear-gradient(90deg,#2f2d2b 0%,#55504a 50%,#2f2d2b 100%)}
.band-dark .shade{position:absolute;inset:0;background:rgba(25,25,25,.45)}
.band-light{background:var(--soft)}
.icon-row{display:flex;align-items:center}
.icon-row .dash{width:200px;border-top:2px dashed rgba(255,255,255,.7);margin:0 20px}
.band-light .icon-row .dash{border-color:#bdbdbd}
.icon-row svg{width:56px;height:56px}
.band-title{font-size:40px;font-weight:300;color:var(--green);text-transform:uppercase}
.band-text{font-size:12.5px;line-height:18px;color:var(--paper)}
.band-light .band-text{color:var(--ink)}

.massage{top:1151px;height:306px}
.skin{top:1457px;height:300px}
.podiatry{top:1757px;height:280px}
.laser{top:2037px;height:306px}
.injections{top:2343px;height:300px}

/* contact */
.contact{top:2643px;height:423px;background:var(--paper)}
.form{left:171px;top:231px;width:552px;height:150px;background:var(--soft)}
.field{position:absolute;left:20px;width:240px;border-bottom:1px solid #d6d6d6;font-size:11px;color:var(--muted);text-transform:uppercase;padding-bottom:6px}
.message{position:absolute;left:280px;top:16px;width:252px;height:84px;border:1px solid #d6d6d6;font-size:11px;color:var(--muted);padding:8px;text-transform:uppercase}
.form .btn{left:435px;top:110px;width:114px;height:30px;font-size:12px}
.info{left:734px;width:295px;background:var(--panel);padding:12px 12px 0 62px}
.info svg{position:absolute;left:20px;top:14px;width:28px;height:28px}
.info .label{font-size:13px;color:var(--muted);text-transform:uppercase}
.info .value{font-size:24px;font-weight:300;color:var(--green);margin-top:2px;white-space:nowrap}
.info .value.small{font-size:14px;margin-top:8px}

/* map */
.map{top:3066px;height:234px}
.map .photo{background:linear-gradient(180deg,#4a4a4a 0%,#3e3e3e 100%)}
.zoom{left:176px;display:flex;align-items:center;gap:12px;color:var(--paper);font-size:13px;text-transform:uppercase}
.zoom svg{width:30px;height:30px}
.map .sec-title{color:var(--paper);font-size:32px}
.map .sec-sub{color:#cfcfcf}
.map-rule{left:430px;top:176px;width:340px;height:1px;background:rgba(255,255,255,.5)}

/* footer */
.footer{top:3300px;height:129px;background:var(--footer)}
.copy{left:171px;top:56px;font-size:12px;color:var(--muted)}
.foot-brand{top:52px;font-size:17px;font-weight:400;color:var(--green)}
.social{right:186px;top:48px;display:flex;gap:14px}
.social span{width:32px;height:32px;border-radius:50%;display:block}
</style>
</head>
<body>

<header class="hero">
  <div class="photo" role="img" aria-label="Softly lit photograph of a client relaxing during a spa massage"></div>
  <div class="shade"></div>
  <div class="abs nav-brand">Fernhill Skin Studio</div>
  <ul class="abs nav">
    <li>Cosmetic Injections</li><li>Podiatry</li><li>Remedial Massage</li><li>Laser Therapies</li><li>Skin Care</li><li>Special Offers</li>
  </ul>
  <div class="abs nav-rule"></div>
  <div class="abs center hero-brand">Fernhill Skin Studio</div>
  <div class="abs center hero-tag">WE ARE COMMITTED TO PROVIDING A QUALITY SERVICE IN AN ATMOSPHERE THAT IS</div>
  <div class="abs center hero-title">RELAXED AND INVITING !</div>
  <div class="abs btn">Book an appointment</div>
</header>

<section class="welcome">
  <div class="abs mark" style="left:583px;top:60px"></div>
  <h2 class="abs center sec-title" style="top:118px">Welcome to the Fernhill</h2>
  <div class="abs center sec-sub" style="top:192px">Skin Studio</div>

  <div class="service" style="left:171px">
    <svg viewBox="0 0 100 100" fill="none" stroke="#33a6d7" stroke-width="2.5" stroke-linecap="round" stroke-linejoin="round">
      <path d="M20 80 L32 68"/><path d="M30 58 L42 70 L78 34 L66 22 Z"/><path d="M60 16 L84 40"/><path d="M72 22 L78 28"/><path d="M40 56 L44 60 M48 48 L52 52 M56 40 L60 44"/><path d="M22 88 q-4 6 0 8 q4 -2 0 -8z"/>
    </svg>
    <h3>Injections</h3>
    <p>Expert injectables for natural, refreshed results, delivered with care by qualified clinicians.</p>
  </div>
  <div class="service" style="left:394px">
    <svg viewBox="0 0 100 100" fill="none" stroke="#33a6d7" stroke-width="2.5" stroke-linecap="round" stroke-linejoin="round">
      <path d="M34 30 C28 50 30 70 40 86 C48 96 64 92 64 80 C64 68 58 62 60 48 C62 36 66 30 60 26 C52 22 40 24 34 30 Z"/>
      <circle cx="34" cy="18" r="5"/><circle cx="45" cy="13" r="4"/><circle cx="55" cy="13" r="3.5"/><circle cx="64" cy="16" r="3"/><circle cx="71" cy="22" r="2.5"/>
    </svg>
    <h3>Podiatry</h3>
    <p>Complete foot health for every stage of life, from routine care to orthotics.</p>
  </div>
  <div class="service" style="left:617px">
    <svg viewBox="0 0 100 100" fill="none" stroke="#33a6d7" stroke-width="2.5" stroke-linecap="round" stroke-linejoin="round">
      <path d="M50 86 L16 52 C4 40 12 18 30 18 C40 18 46 24 50 30 C54 24 60 18 70 18 C88 18 96 40 84 52 Z"/>
      <path d="M14 54 H36 L42 42 L50 66 L58 48 L62 54 H86"/>
    </svg>
    <h3>Care</h3>
    <p>Personal plans built around you, with time to listen and unhurried follow up.</p>
  </div>
  <div class="service" style="left:837px">
    <svg viewBox="0 0 100 100" fill="none" stroke="#33a6d7" stroke-width="2.5" stroke-linecap="round">
      <circle cx="50" cy="50" r="10"/>
      <path d="M50 10 V32 M50 68 V90 M10 50 H32 M68 50 H90 M22 22 L36 36 M64 64 L78 78 M78 22 L64 36 M36 64 L22 78"/>
    </svg>
    <h3>Treatments</h3>
    <p>Laser, IPL and skin therapies chosen to suit your skin and your goals.</p>
  </div>
</section>

<section class="massage band-dark">
  <div class="photo" role="img" aria-label="Photograph of a remedial massage on a client's back"></div>
  <div class="shade"></div>
  <div class="abs icon-row" style="left:426px;top:58px">
    <span class="mark"></span><span class="dash"></span>
    <svg viewBox="0 0 60 60" fill="none" stroke="#fff" stroke-width="2" stroke-linecap="round" stroke-linejoin="round"><path d="M6 44 H54"/><path d="M10 44 C14 36 24 34 34 36 L48 38"/><circle cx="40" cy="20" r="5"/><path d="M40 26 L34 36 M38 28 L48 34"/></svg>
  </div>
  <h2 class="abs center band-title" style="top:126px">Remedial Massage !</h2>
  <p class="abs band-text" style="left:280px;width:640px;top:190px;text-align:center">Release tension and restore easy movement with remedial massage tailored to your body. Our therapists assess posture and muscle tightness, then work with focused, deep techniques to ease pain, speed recovery and leave you feeling lighter, calmer and properly rested.</p>
</section>

<section class="skin band-light">
  <div class="abs" role="img" aria-label="Photograph of two women in towel turbans wearing face masks" style="left:171px;top:0;width:429px;height:300px;background:linear-gradient(135deg,#e3c3b2 0%,#d9a79a 45%,#e9c56e 100%)"></div>
  <div class="abs icon-row" style="left:650px;top:50px">
    <span class="mark"></span><span class="dash" style="width:160px"></span>
    <svg viewBox="0 0 60 60" fill="none" stroke="#33a6d7" stroke-width="2" stroke-linecap="round" stroke-linejoin="round"><path d="M20 54 C10 42 12 18 30 12 C44 8 54 20 50 34 C48 42 44 50 44 54"/><path d="M34 30 q4 -2 8 0"/></svg>
  </div>
  <h2 class="abs band-title" style="left:600px;width:460px;top:112px;text-align:center">Skin Care !</h2>
  <p class="abs band-text" style="left:610px;width:440px;top:170px;text-align:center">Clinical facials and medical grade products that renew tired skin. Each program begins with a detailed skin analysis, so every step is matched to your skin type, concerns and the results you want to see.</p>
</section>

<section class="podiatry band-dark">
  <div class="photo" role="img" aria-label="Photograph of a foot treatment in a spa room"></div>
  <div class="shade"></div>
  <div class="abs icon-row" style="left:426px;top:42px">
    <span class="mark"></span><span class="dash"></span>
    <svg viewBox="0 0 60 60" fill="none" stroke="#fff" stroke-width="2" stroke-linecap="round" stroke-linejoin="round"><path d="M20 20 C16 32 18 44 24 52 C30 58 40 56 40 48 C40 40 36 36 38 28 C40 20 40 16 36 14 C30 12 24 14 20 20 Z"/><circle cx="20" cy="10" r="3"/><circle cx="28" cy="7" r="2.5"/><circle cx="35" cy="7" r="2"/><circle cx="41" cy="10" r="2"/></svg>
  </div>
  <h2 class="abs center band-title" style="top:112px">Podiatry</h2>
  <p class="abs band-text" style="left:280px;width:640px;top:176px;text-align:center">Our podiatrists treat heel pain, corns, ingrown nails and sports injuries with gentle, evidence based care. We look at the way you stand and walk, explain every option clearly and help you keep your feet comfortable, strong and active for years.</p>
</section>

<section class="laser band-light">
  <div class="abs icon-row" style="left:180px;top:50px">
    <span class="mark"></span><span class="dash" style="width:180px"></span>
    <svg viewBox="0 0 60 60" fill="none" stroke="#33a6d7" stroke-width="2" stroke-linecap="round"><circle cx="30" cy="30" r="6"/><path d="M30 6 V20 M30 40 V54 M6 30 H20 M40 30 H54 M13 13 L22 22 M38 38 L47 47 M47 13 L38 22 M22 38 L13 47"/></svg>
  </div>
  <h2 class="abs band-title" style="left:140px;width:460px;top:118px;text-align:center">Laser Treatment</h2>
  <p class="abs band-text" style="left:160px;width:420px;top:176px;text-align:center">Laser and IPL therapies reduce pigmentation, redness, fine lines and unwanted hair. Treatments are quick and comfortable, performed on modern equipment by trained clinicians who tailor every setting to your skin.</p>
  <div class="abs" role="img" aria-label="Photograph of a client receiving a laser facial treatment" style="left:657px;top:0;width:372px;height:306px;background:linear-gradient(135deg,#f3ede8 0%,#dcc4b4 50%,#8e7b6e 100%)"></div>
</section>

<section class="injections band-dark">
  <div class="photo" role="img" aria-label="Photograph of hands during a cosmetic treatment"></div>
  <div class="shade"></div>
  <div class="abs icon-row" style="left:426px;top:52px">
    <span class="mark"></span><span class="dash"></span>
    <svg viewBox="0 0 60 60" fill="none" stroke="#fff" stroke-width="2" stroke-linecap="round" stroke-linejoin="round"><path d="M8 52 L16 44"/><path d="M14 38 L22 46 L46 22 L38 14 Z"/><path d="M34 8 L52 26"/><path d="M42 14 L46 18"/></svg>
  </div>
  <h2 class="abs center band-title" style="top:122px">Cosmetics Injections</h2>
  <p class="abs band-text" style="left:280px;width:640px;top:186px;text-align:center">Anti wrinkle injections and dermal fillers, planned with a light touch for soft, natural results. Every consultation is unhurried and private, with honest advice about what will suit your face and a clear plan for ongoing care and review.</p>
</section>

<section class="contact">
  <div class="abs mark" style="left:583px;top:43px"></div>
  <h2 class="abs center sec-title" style="top:110px">Contact us now !</h2>
  <div class="abs center sec-sub" style="top:184px">Skin Studio</div>
  <div class="abs form">
    <div class="field" style="top:16px">Name</div>
    <div class="field" style="top:50px">Email</div>
    <div class="field" style="top:84px">Phone</div>
    <div class="message">Message</div>
    <div class="abs btn">Send</div>
  </div>
  <div class="abs info" style="top:231px;height:70px">
    <svg viewBox="0 0 30 30" fill="none" stroke="#33a6d7" stroke-width="2" stroke-linecap="round" stroke-linejoin="round"><path d="M8 4 L12 10 L9 13 C11 17 13 19 17 21 L20 18 L26 22 L23 27 C14 26 4 16 3 7 Z"/></svg>
    <div class="label">Call us now !</div>
    <div class="value">0800 (555) 0192</div>
  </div>
  <div class="abs info" style="top:311px;height:70px">
    <svg viewBox="0 0 30 30" fill="none" stroke="#33a6d7" stroke-width="2" stroke-linejoin="round"><rect x="3" y="7" width="24" height="16"/><path d="M3 7 L15 17 L27 7"/></svg>
    <div class="label">Send us mail !</div>
    <div class="value small">hello@fernhillskinstudio.com</div>
  </div>
</section>

<section class="map">
  <div class="photo" role="img" aria-label="Street map showing the studio location"></div>
  <div class="abs zoom" style="top:36px">
    <svg viewBox="0 0 30 30" fill="none" stroke="#fff" stroke-width="2"><circle cx="15" cy="15" r="13"/><path d="M9 15 H21 M15 9 V21"/></svg>Zoom in
  </div>
  <div class="abs zoom" style="top:80px">
    <svg viewBox="0 0 30 30" fill="none" stroke="#fff" stroke-width="2"><circle cx="15" cy="15" r="13"/><path d="M9 15 H21"/></svg>Zoom out
  </div>
  <div class="abs mark" style="left:583px;top:56px"></div>
  <h2 class="abs center sec-title" style="top:122px">Location map</h2>
  <div class="abs map-rule"></div>
  <div class="abs center sec-sub" style="top:188px">Skin Studio</div>
</section>

<footer class="footer">
  <div class="abs copy">© Copyright Fernhill Skin Studio 2014</div>
  <div class="abs center foot-brand">Fernhill Skin Studio</div>
  <div class="abs social">
    <span style="background:var(--blue)"></span>
    <span style="background:var(--blue)"></span>
    <span style="background:var(--green)"></span>
    <span style="background:var(--green)"></span>
  </div>
</footer>

</body>
</html>
```